Qarnetix EIRL Business Card Design Project

We need a business card design for a New Business Intelligence Consultant. We bring a complete service to the client from first consulting meeting to help desk and system improvement.

I will upload the company logo and I like to use the logo colors on the card. Feel free to use all logo components on the design, for example one side with the black logo using complete card and the other side only the red shape (is an example, feel absolutely free :)).

The principal idea is to sell a professional service and a modern company.

Target Market(s)

IT Business Intelligence Clients

Industry/Entity Type

Professional Service

Requirements
Nice to have
• - Use the logo colors and minimize white sections.
- Rounded borders
Should not have
• I don't want to see any references to people working on a meeting or office photos or any computers related logos.

```html
<!DOCTYPE html>
<html lang="en">
<head>
<meta charset="utf-8">
<title>Qarnetix EIRL – Business Card</title>
<link rel="stylesheet" href="https://fonts.googleapis.com/css2?family=Source+Sans+3:wght@400;600;700&display=swap">
<style>
  :root {
    --stage: #e9e6df;
    --card: #000000;
    --red: #ed1c24;
    --grey: #a7a9ac;
    --text: #ffffff;
    --label: #bcbec0;
    --radius: 19px;
  }
  * { margin: 0; padding: 0; box-sizing: border-box; }
  html, body {
    width: 1200px; height: 686px; overflow: hidden;
    background: var(--stage);
    font-family: "Source Sans 3", "Segoe UI", sans-serif;
  }
  .stage { position: relative; width: 1200px; height: 686px; }

  .card {
    position: absolute;
    width: 526px; height: 300px;
    background: var(--card);
    border-radius: var(--radius);
    overflow: hidden;
    color: var(--text);
  }
  .card--front { left: 57px; top: 135px; }
  .card--back  { left: 610px; top: 268px; }

  .brand {
    position: absolute; left: 0; right: 0;
    display: flex; align-items: center; justify-content: center; gap: 14px;
  }
  .brand__square { background: var(--red); display: block; }
  .brand__name {
    color: var(--grey); font-weight: 400; letter-spacing: 0.5px; line-height: 1;
  }
  .card--front .brand { top: 82px; }
  .card--front .brand__square { width: 34px; height: 34px; }
  .card--front .brand__name { font-size: 50px; }
  .card--back .brand { top: 112px; }
  .card--back .brand__square { width: 44px; height: 44px; }
  .card--back .brand__name { font-size: 62px; }

  .contact {
    position: absolute; left: 0; right: 0; top: 150px;
    text-align: center; font-size: 13.5px; line-height: 21px;
  }
  .contact__name-line { display: flex; justify-content: center; align-items: baseline; gap: 8px; margin-bottom: 2px; }
  .contact__name { color: var(--red); font-weight: 700; font-size: 17px; }
  .contact__divider { width: 1px; height: 12px; background: var(--red); align-self: center; }
  .contact__title { color: var(--label); font-weight: 600; font-size: 13px; }
  .contact__row { display: flex; justify-content: center; gap: 18px; }
  .contact__item { display: inline-flex; align-items: center; gap: 2px; }
  .contact__item svg { width: 12px; height: 12px; fill: var(--red); }
  .contact__at { color: var(--red); font-weight: 700; font-size: 15px; }

  .bands { position: absolute; left: 0; bottom: 0; width: 526px; height: 27px; display: block; }
  .card--back .bands { height: 26px; }
</style>
</head>
<body>
<main class="stage">

  <section class="card card--front" aria-label="Card front">
    <div class="brand">
      <span class="brand__square"></span>
      <span class="brand__name">qarnetix</span>
    </div>

    <div class="contact">
      <p class="contact__name-line">
        <span class="contact__name">Your Name</span>
        <span class="contact__divider"></span>
        <span class="contact__title">Title</span>
      </p>
      <p>Complex name,Street name City, State, zip code</p>
      <p class="contact__row">
        <span class="contact__item">
          <svg viewBox="0 0 24 24" aria-hidden="true"><path d="M6.6 10.8a15 15 0 0 0 6.6 6.6l2.2-2.2a1 1 0 0 1 1-.25 11.4 11.4 0 0 0 3.6.57 1 1 0 0 1 1 1V20a1 1 0 0 1-1 1A17 17 0 0 1 3 4a1 1 0 0 1 1-1h3.5a1 1 0 0 1 1 1c0 1.25.2 2.45.57 3.57a1 1 0 0 1-.25 1z"/></svg>123-456-7890
        </span>
        <span class="contact__item">
          <svg viewBox="0 0 24 24" aria-hidden="true"><path d="M7 2h10v5H7zM3 8h18v9h-4v5H7v-5H3zm6 8v4h6v-4z"/></svg>123-456-7890
        </span>
      </p>
      <p class="contact__row">
        <span class="contact__item"><span class="contact__at">@</span>name@website.com</span>
        <span class="contact__item">
          <svg viewBox="0 0 24 24" aria-hidden="true"><path d="M12 2a10 10 0 1 0 0 20 10 10 0 0 0 0-20zm0 2c.9 0 2.1 1.7 2.7 5H9.3C9.9 5.7 11.1 4 12 4zM4.3 9h3c-.1.6-.1 1.3-.1 2v1H4.1a8 8 0 0 1 .2-3zm-.2 4h3.1c0 .7.1 1.4.2 2h-2.6a8 8 0 0 1-.7-2zm5.1 0h5.6a16 16 0 0 1-.2 2H9.4a16 16 0 0 1-.2-2zm0-2c0-.7 0-1.4.1-2h5.4c.1.6.1 1.3.1 2zm7.6 2h3.1a8 8 0 0 1-.7 2h-2.6c.1-.6.2-1.3.2-2zm0-2v-1c0-.7 0-1.4-.1-2h3a8 8 0 0 1 .2 3zM9.5 17h5c-.6 1.9-1.6 3-2.5 3s-1.9-1.1-2.5-3z"/></svg>www.website.com
        </span>
      </p>
    </div>

    <svg class="bands" viewBox="0 0 526 27" preserveAspectRatio="none" aria-hidden="true">
      <polygon points="0,0 377,0 407,27 0,27" fill="var(--red)"/>
      <polygon points="385,0 526,0 526,27 415,27" fill="var(--grey)"/>
    </svg>
  </section>

  <section class="card card--back" aria-label="Card back">
    <div class="brand">
      <span class="brand__square"></span>
      <span class="brand__name">qarnetix</span>
    </div>

    <svg class="bands" viewBox="0 0 526 26" preserveAspectRatio="none" aria-hidden="true">
      <polygon points="0,0 144,0 114,26 0,26" fill="var(--grey)"/>
      <polygon points="151,0 526,0 526,26 121,26" fill="var(--red)"/>
    </svg>
  </section>

</main>
</body>
</html>
```